New River III Precinct 6x11 GOTV postcard

We require BOTH persuasive copy and high-impact layout for an oversized 6x11 political mailer. This might be one person, but it likely requires a specialized "creative team." of an experienced political strategist copywriter PLUS a graphic designer - so the words fit the exact layout block, and the visuals reinforce the psychological punch of the headline.

The goal is to remove all excuses a targeted audience of ~900 registered Harvestline + ~1800 Unaffiliated voters in our precinct - have for not voting.

I need to be able to work by phone / online chat to iterate designs
I need to own the design in the top couple of software outputs that any printer service will require.

I want to experiment with very subtle background images as follows:
- Front of postcard that conveys "CHANGE" of not just seasons - but of encouraging change of precinct voter representation - so anything about fall foliage / conveyance of change tie-in is worthy of considering
- Back of postcard - any Appalachian long rage mountain view that includes 5-7 layers of hills in the distance.
Some photos as samples to consider.

Target Market(s)

~2,700 registered Harvestliners and Unaffiliated voters

Requirements
Must have
• We require BOTH persuasive copy and high-impact layout for an oversized 6x11 political mailer. This might be one person, but it likely requires a specialized "creative team." of an experienced political strategist copywriter PLUS a graphic designer - so the words fit the exact layout block, and the visuals reinforce the psychological punch of the headline
Nice to have
• subtle background photos

```html
<!DOCTYPE html>
<html lang="en">
<head>
<meta charset="utf-8">
<title>New River III Precinct GOTV Postcard</title>
<link rel="stylesheet" href="https://fonts.googleapis.com/css2?family=Roboto+Condensed:wght@400;700&display=swap">
<style>
  :root {
    --page-bg: #e6e6e6;
    --card-red: #9a1c20;
    --card-navy: #111d45;
    --card-white: #ffffff;
    --ink: #1b1b1b;
    --text-light: #ffffff;
    --flag-red: 179, 35, 43;
    --flag-blue: 30, 45, 107;
    --stamp-line: #222222;
  }
  * { box-sizing: border-box; margin: 0; padding: 0; }
  html, body { width: 1200px; height: 1200px; overflow: hidden; }
  body {
    background: var(--page-bg);
    font-family: "Roboto Condensed", "Arial Narrow", sans-serif;
    position: relative;
  }
  .postcard {
    position: absolute;
    left: 136px;
    width: 926px;
    height: 505px;
    overflow: hidden;
  }
  .postcard--front { top: 80px; display: flex; }
  .postcard--back { top: 619px; background: var(--card-white); }

  /* FRONT */
  .issues-panel {
    position: relative;
    width: 553px;
    height: 100%;
    background: var(--card-red);
    color: var(--text-light);
    padding: 40px 28px 0 42px;
    overflow: hidden;
  }
  .issues-panel__flag {
    position: absolute;
    left: 0; bottom: 0;
    width: 340px; height: 340px;
    background:
      radial-gradient(ellipse at 5% 98%, rgba(10,10,20,0.85) 0%, rgba(40,10,20,0.45) 35%, rgba(0,0,0,0) 68%);
  }
  .issues-panel__content { position: relative; }
  .headline {
    font-size: 29px;
    font-weight: 700;
    text-decoration: underline;
    text-decoration-thickness: 2px;
    text-underline-offset: 4px;
    margin-bottom: 20px;
  }
  .issue { font-size: 11.4px; line-height: 15px; margin-bottom: 11px; }
  .issue--tight { margin-bottom: 0; }
  .issue strong { font-weight: 700; }

  .ballot-panel {
    width: 373px;
    height: 100%;
    background: var(--card-navy);
    color: var(--text-light);
    padding: 42px 24px 0 46px;
  }
  .ballot-panel__title { font-size: 11.4px; font-weight: 700; margin-bottom: 20px; }
  .race { font-size: 11.4px; line-height: 14px; margin-bottom: 14.5px; }
  .race__name { display: block; font-weight: 700; }
  .race--measure { font-weight: 700; margin-bottom: 14.5px; padding-bottom: 14px; }

  /* BACK */
  .greeting-bar {
    position: absolute;
    left: 0; top: 41px;
    width: 239px; height: 22px;
    background: var(--card-navy);
    color: var(--text-light);
    font-size: 11.4px;
    font-weight: 700;
    padding: 4px 0 0 42px;
  }
  .letter {
    position: absolute;
    left: 42px; top: 74px;
    width: 516px;
    color: var(--ink);
    font-size: 11.4px;
    line-height: 14px;
  }
  .letter p { margin-bottom: 13.5px; }
  .voter-info {
    position: absolute;
    left: 42px; top: 309px;
    color: var(--ink);
    font-size: 11.4px;
    line-height: 14px;
    list-style: none;
  }
  .voter-info li { margin-bottom: 6.5px; }
  .stamp-box {
    position: absolute;
    left: 758px; top: 48px;
    width: 107px; height: 124px;
    border: 1.5px solid var(--stamp-line);
  }
  .flag-art {
    position: absolute;
    left: 300px; top: 240px;
    width: 350px; height: 270px;
    background:
      radial-gradient(ellipse 30% 26% at 30% 70%, rgba(var(--flag-blue), 0.55) 0%, rgba(var(--flag-blue), 0) 100%),
      radial-gradient(ellipse 50% 50% at 55% 50%, rgba(var(--flag-red), 0.45) 0%, rgba(var(--flag-red), 0.2) 55%, rgba(var(--flag-red), 0) 100%);
  }
</style>
</head>
<body>
  <section class="postcard postcard--front">
    <div class="issues-panel">
      <div class="issues-panel__flag" role="img" aria-label="Dark waving American flag with stars fading into the red background"></div>
      <div class="issues-panel__content">
        <h1 class="headline">VOTE FOR NEW REPRESENTATION</h1>
        <p class="issue"><strong>LOCAL PAIN-THANKS TO CURRENT REPRESENTATIVES</strong> - and sadly, to avoid accountability, they've cleverly delayed many / most impacts until AFTER the 2026 election. <strong>VOTE FOR CHANGE</strong></p>
        <p class="issue"><strong>FAMILY BUDGET:</strong> exploded costs for everything: groceries, gas, car insurance, rent.</p>
        <p class="issue"><strong>HEALTH</strong> - expired subsidies, tax credits mean ~1m in NC will lose coverage or pay more. 50% cuts to Hospitals, Mental Health facilities; rural facilities will be closing</p>
        <p class="issue issue--tight"><strong>REPRODUCTIVE RIGHTS</strong> - Government authoritarian intrusion - censure women's rights.</p>
        <p class="issue issue--tight"><strong>FOOD SECURITY</strong> - Weaponized Hunger-cuts to SNAP; school meals cut; add'l work reqmts</p>
        <p class="issue"><strong>EDUCATION</strong> - Watauga $2.2mm shortfall personnel cuts, freezes in hiring, teacher training. Abandoning civil rights of Special Ed students to HHS and DOL</p>
        <p class="issue"><strong>HOUSING</strong> - ~25% of renters are spending over 50% of income on rent. Especially bad locally; predatory leasing terms and skyrocketing rents. Proposed legislation is transforming HUD with the goal of getting rid of Section 8 housing that cares for vulnerable populations.</p>
        <p class="issue"><strong>ENERGY</strong> - In 2022 Boone achieved 100% renewable energy in town buildings; this is now being destroyed by repeal of renewable energy project funding; Highland State Innovation District prepares renewable workforce technologies-all this is now in limbo.</p>
        <p class="issue"><strong>ENVIRONMENT</strong> - Reduced protections from coal ash pond leaks threaten public health. Corporations not held responsible for damage; public picks up the tab. Environmental Justice enforcement no longer a priority. Logging in Watauga with no public oversight. It's the "haz-mat" model do nothing, wait for catastrophe, then fix it</p>
      </div>
    </div>
    <aside class="ballot-panel">
      <h2 class="ballot-panel__title">SAMPLE BALLOT RECOMMENDATIONS</h2>
      <p class="race">US SENATE -<span class="race__name">RAY CALLOWAY</span></p>
      <p class="race">US HOUSE -DISTRICT 5-<span class="race__name">CHET HALVORSEN</span></p>
      <p class="race race--measure">REQMT TO SHOW ID FOR VOTERS NOT IN PERSON-NO</p>
      <p class="race">STATE SENATE DISTRICT 47-<span class="race__name">FRANK MARLOWE</span></p>
      <p class="race">HOUSE OF REP'S DISTRICT 93-<span class="race__name">CHARLIE DENHOLM</span></p>
      <p class="race">NC SUPREME COURT<span class="race__name">ANITA VERHOEF</span></p>
      <p class="race">NC COURT OF APPEALS-SEAT 1<span class="race__name">JOHN ASHCOMBE</span></p>
      <p class="race">NC COURT OF APPEALS-SEAT 2-<span class="race__name">TOBY RENNICK</span></p>
      <p class="race">NC COURT OF APPEALS-SEAT 3-<span class="race__name">CHRISTINE OBERLIN</span></p>
    </aside>
  </section>

  <section class="postcard postcard--back">
    <div class="greeting-bar">Dear New River III Neighbor.</div>
    <div class="flag-art" role="img" aria-label="Waving American flag illustration in red, white and blue"></div>
    <div class="letter">
      <p>We live in a representative democracy. We expect our representatives will exercise independent thinking and support policies and legislation that don't harm us - and that reflect the MAJORITY VIEWS of precinct citizens.</p>
      <p>But our current representatives HAVE STOPPED LISTENING - they are now bringing harmful policies straight to Watauga County. IT'S TIME TO HOLD THEM ACCOUNTABLE AND VOTE THEM OUT.</p>
      <p>Make no mistake: in 2026, every election is partisan. Even Judicial seats are now tied directly to state platforms.</p>
      <p>Any candidate who refuses to publicly condemn Raleigh's gerrymandered overreach into Watauga politics-or refuses to fight funding cuts for our healthcare, education, and environmental justice - is actively supporting these harmful policies.</p>
      <p>They are hoping their silence fools you. DON'T BE FOOLED. This November, VOTE FOR CHANGE.</p>
    </div>
    <ul class="voter-info">
      <li>YOU ARE A REGISTERED VOTER IN WATAUGA COUNTY</li>
      <li>YOU RESIDE IN PRECINCT: NEW RIVER III</li>
      <li>POLLING PLACES AVAILABLE TO YOU ARE: LOCATION,. 2, 3</li>
      <li>EARLY VOTING STARTS ON:</li>
      <li>DEADLINE TO APPLY FOR MAIL-IN BALLOTS</li>
      <li>KNOW THE RULES TO ENSURE YOUR MAIL-IN-BALLOT COUNTS</li>
    </ul>
    <div class="stamp-box"></div>
  </section>
</body>
</html>
```